Upstart Retirement Planning Firm needs help with business card design

Harborlight Wealth Partners, LLC is looking for help with business card design. We give advice on investments, insurance, and other financial matters related to retirement. There are some required disclosures that we will provide but mostly we are looking for a professional, classy business card that reflects the theme we have chosen. We have a logo that is attached but we would like to add a phrase; "Shaping Your Working Years Into Lasting Security"

Doubled sided only so that we can add the required disclosures (needed for our industry) on the back of the card. We will provide the exact words for this in 1-2 days.

Target Market(s)

Retirees and Pre-retirees. Professionals 50+ years old

Industry/Entity Type

Financial Planning

Contact Information for Business Card

We currently have two people who will need separate cards so we'd like to have a template so that we can add names for new cards in the future.

For the first run, please show the following information.

Neil Osgood, MBA, ChFC®, CLU®
Financial Advisor, Registered Representative
nosgood@harborlightwp.example
Phone: (555) 218-3960
Toll Free Fax: (555) 218-3961

Address is
2876 Meadowbrook Pkwy.
Suite K418
Virginia Beach, VA 23019

Colors
3277b5

Requirements
Must have
• Logo, contact info, small phase to describe business (in description), required legal disclosures on back of the card as follows (in small font)
• Neil Osgood is a registered representative of and offers securities through Brightwater Capital Brokerage Corporation, Member SIPC. Brightwater Capital Brokerage Corporation is a member of the Brightwater Advisory Group which is the marketing name for Brightwater Holding Corporation and its affiliates.
Nice to have
• Rounded edges, raised letters
Should not have
• any colors that aren't in the logo (other than black for font)

```html
<!DOCTYPE html>
<html lang="en">
<head>
<meta charset="utf-8">
<title>Harborlight Wealth Partners – Business Card</title>
<link rel="stylesheet" href="https://fonts.googleapis.com/css2?family=Source+Sans+3:ital,wght@0,400;0,600;1,600;1,700&display=swap">
<style>
  :root {
    --backdrop: #000000;
    --card: #333437;
    --brand-blue: #3266b0;
    --text-light: #f2f2f2;
  }
  html, body {
    margin: 0;
    padding: 0;
    width: 1200px;
    height: 900px;
    overflow: hidden;
    background: var(--backdrop);
    font-family: "Source Sans 3", "Myriad Pro", sans-serif;
  }
  .stage {
    position: relative;
    width: 1200px;
    height: 900px;
  }
  .card {
    position: absolute;
    top: 271px;
    width: 457px;
    height: 281px;
    border-radius: 14px;
    background: var(--card);
    box-sizing: border-box;
  }
  .card--front { left: 137px; }
  .card--back { left: 626px; }

  /* front */
  .wordmark {
    position: absolute;
    left: 22px;
    top: 34px;
    margin: 0;
    color: var(--brand-blue);
    font-weight: 600;
    font-size: 22px;
    letter-spacing: 0.2px;
  }
  .contact {
    position: absolute;
    left: 180px;
    top: 104px;
    color: var(--text-light);
    font-size: 13px;
    line-height: 1.5;
  }
  .contact__name {
    margin: 0;
    color: var(--brand-blue);
    font-size: 16.5px;
    font-weight: 600;
    line-height: 1.2;
  }
  .contact__credentials { font-size: 11.5px; }
  .contact__title { margin: 2px 0 10px; }
  .contact__line {
    display: flex;
    align-items: center;
    gap: 7px;
    margin: 0;
  }
  .contact__icon { width: 9px; height: 9px; fill: var(--brand-blue); }
  .contact__fax { margin: 0; font-weight: 600; }
  .contact__label { color: var(--brand-blue); }
  .contact__address { margin: 11px 0 0; }

  /* back */
  .back__name {
    position: absolute;
    left: 0;
    right: 0;
    top: 98px;
    margin: 0;
    text-align: center;
    color: var(--brand-blue);
    font-weight: 600;
    font-size: 28px;
  }
  .back__tagline {
    position: absolute;
    left: 0;
    right: 0;
    top: 195px;
    margin: 0;
    text-align: center;
    color: var(--text-light);
    font-style: italic;
    font-weight: 700;
    font-size: 15.5px;
  }
</style>
</head>
<body>
<main class="stage">
  <section class="card card--front" aria-label="Card front">
    <p class="wordmark">Harborlight Wealth Partners</p>
    <div class="contact">
      <h1 class="contact__name">Neil Osgood, MBA<span class="contact__credentials">, ChFC®, CLU®</span></h1>
      <p class="contact__title">Financial Advisor, Registered Representative</p>
      <p class="contact__line">
        <svg class="contact__icon" viewBox="0 0 10 10" aria-hidden="true"><path d="M2 0.5 L3.6 2.6 L2.8 3.6 Q4 6 6.4 7.2 L7.4 6.4 L9.5 8 L8.3 9.5 Q1 8 0.5 1.7 Z"/></svg>
        (555) 218-3960
      </p>
      <p class="contact__line">
        <svg class="contact__icon" viewBox="0 0 10 10" aria-hidden="true"><path d="M0.5 2 H9.5 V8 H0.5 Z M0.8 2.3 L5 5.4 L9.2 2.3" stroke="#333437" stroke-width="0.8"/></svg>
        nosgood@harborlightwp.example
      </p>
      <p class="contact__fax"><span class="contact__label">TOLL FREE FAX:</span> (555) 218-3961</p>
      <p class="contact__address">2876 Meadowbrook Pkwy. Suite K418<br>Virginia Beach, VA 23019</p>
    </div>
  </section>

  <section class="card card--back" aria-label="Card back">
    <h2 class="back__name">Harborlight Wealth Partners, LLC</h2>
    <p class="back__tagline">Shaping Your Working Years Into Lasting Security</p>
  </section>
</main>
</body>
</html>
```